velmora LED lighting Brochure design *

need a Brochure for velmora LED, that is a company specialises in industrial LED lighting solutions ... we also do retail, gas stations as well...
we are formed to serve customer need in lighting doing engineering, supply and installation of LED lighting
we need a Brochure that describe our company work, project cycle, project reference and services provided in addition to our main products that will be provided to consultant for product range approval

Target Market(s)

industrial sector (petrochemical, chemical, factories), construction, retail shops, gas stations

Industry/Entity Type

Lighting

Colors

Requirements
Must have
• project cycle
• project reference photos... cant upload it here

```html
<!DOCTYPE html>
<html lang="en">
<head>
<meta charset="utf-8">
<title>velmora LED lighting – Brochure</title>
<link href="https://fonts.googleapis.com/css2?family=Roboto+Condensed:wght@400;700&family=Open+Sans:wght@400;600&family=Cairo:wght@600&display=swap" rel="stylesheet">
<style>
:root{
  --navy:#17304c;
  --navy-dark:#122840;
  --teal:#2b9ab8;
  --red:#e3222b;
  --yellow:#f6c21c;
  --white:#ffffff;
  --ink:#2c3440;
  --muted:#8a95a3;
  --bg:#e8e9eb;
  --line:#4f6f8f;
  --s1:#2d6a96;--s2:#4fb0d2;--s3:#36a04a;--s4:#8cc63f;--s5:#f3b417;
  --s6:#f0881d;--s7:#e3222b;--s8:#17304c;--s9:#3591cd;
}
*{box-sizing:border-box;margin:0;padding:0}
html,body{width:1200px;height:3511px;overflow:hidden}
body{background:var(--bg);font-family:"Open Sans",sans-serif;position:relative}
.sheet-grid{position:absolute;left:60px;top:607px;display:grid;grid-template-columns:520px 520px;grid-auto-rows:732px;gap:50px 40px}
.page{position:relative;width:520px;height:732px;overflow:hidden;background:var(--white);box-shadow:0 2px 10px rgba(0,0,0,.12)}
.page--navy{background:var(--navy)}
.abs{position:absolute}
.head{font-family:"Roboto Condensed",sans-serif;font-weight:700}

.brand{position:absolute;display:flex;align-items:center;gap:14px}
.brand__name{font-family:"Roboto Condensed",sans-serif;font-weight:700;font-size:30px;letter-spacing:5px;line-height:1}
.brand__sub{font-size:6.5px;letter-spacing:.3px;margin-top:3px}
.brand__mark{width:38px;height:38px;border:2px solid currentColor;border-radius:4px}
.brand__ar{font-family:"Cairo",sans-serif;font-weight:600;text-align:right;line-height:1.15}
.brand__ar b{display:block;font-size:19px;font-weight:600}
.brand__ar span{font-size:9px}
.brand--light{color:var(--white)}
.brand--dark{color:var(--navy)}

.photo{position:absolute}

.cover__tag{left:56px;top:205px;font-size:22px;color:var(--teal)}
.cover__photo{left:160px;right:8px;top:390px;bottom:0;border-radius:50px 50px 0 0;background:linear-gradient(160deg,#8fe1f0 0%,#2aa0bd 35%,#0d6c8a 70%,#0a4a63 100%)}
.cover__rule{left:0;top:392px;width:160px;height:1px;background:var(--line)}

.about__title{left:38px;top:150px;height:330px;writing-mode:vertical-rl;transform:rotate(180deg);font-size:64px;color:var(--navy);line-height:1}
.about__panel{left:152px;right:0;top:150px;bottom:52px;background:var(--navy);border-radius:44px 0 0 44px}
.about__band{left:276px;right:0;top:527px;bottom:0;background:var(--red);border-radius:38px 0 0 0}
.about__text{left:190px;right:30px;top:180px;color:var(--white);font-size:8.3px;line-height:1.55}
.about__text p{margin-bottom:9px}
.about__quote{left:190px;top:556px;font-size:19px;color:var(--white);line-height:1.35}
.about__quote .q2{display:block;padding-left:108px;color:var(--yellow)}

.goals__photo{background:linear-gradient(160deg,#1d2f4c,#c58a3a 70%,#3a3026)}
.goals__band{left:0;right:0;top:532px;bottom:0;background:var(--red)}
.goals__title{right:40px;top:494px;font-size:31px;color:var(--red)}
.goals__text{left:60px;right:52px;top:556px;color:var(--white);font-size:8.3px;line-height:1.55;text-align:center}

.refs__title{left:44px;top:52px;color:var(--navy);font-size:23px;line-height:1}
.refs__title span{display:block;color:var(--teal);font-size:40px;margin-top:2px}
.refs__grid{position:absolute;left:40px;right:26px;top:52px;display:grid;grid-template-columns:repeat(4,1fr);grid-auto-rows:102px;column-gap:12px}
.refs__cell{display:flex;flex-direction:column;gap:6px}
.refs__cell--title{grid-column:span 2}
.refs__logo{width:70px;height:26px;border-radius:4px;background:#d9dde3}
.refs__logo--c{width:30px;height:30px;border-radius:50%}
.refs__cap{font-size:6.6px;color:var(--ink);line-height:1.35}

.cycle__intro{left:52px;top:50px;width:210px;font-size:8.3px;line-height:1.45;color:var(--ink)}
.cycle__head{left:276px;top:50px;line-height:.95}
.cycle__head .c1{display:block;font-size:22px;color:var(--teal)}
.cycle__head .c2{display:block;font-size:48px;color:var(--red)}
.cycle__spine{left:250px;top:140px;width:2px;height:560px;background:#c9ced6}
.step{position:absolute;width:218px}
.step--l{left:52px}
.step--r{left:250px;width:220px}
.step__title{font-family:"Roboto Condensed",sans-serif;font-size:12px;letter-spacing:.3px;padding-left:26px;border-bottom:1px solid currentColor}
.step--r .step__title{padding-left:0;padding-right:30px;text-align:right}
.step__box{color:var(--white);font-size:6.6px;line-height:1.4;padding:6px 10px 6px 26px;min-height:42px}
.step--r .step__box{padding:6px 30px 6px 10px}
.step__num{position:absolute;top:10px;width:30px;height:30px;border-radius:50%;background:var(--white);border:3px solid currentColor;font-family:"Roboto Condensed",sans-serif;font-weight:700;font-size:14px;display:flex;align-items:center;justify-content:center;color:var(--navy)}
.step--l .step__num{left:-14px}
.step--r .step__num{right:-14px}

.back__arc{left:0;top:0}
.back__card{left:8px;width:340px;top:452px;bottom:0;background:var(--white);border-radius:60px 60px 0 0}
.back__mark{left:40px;top:40px;width:56px;height:56px;border-radius:6px;background:#c7ccd4}
.back__addr{left:40px;top:115px;font-size:7.6px;line-height:1.5;color:var(--navy)}
</style>
</head>
<body>
<main class="sheet-grid">

  <section class="page page--navy">
    <div class="brand brand--light" style="left:40px;top:40px">
      <div><div class="brand__name">velmora</div><div class="brand__sub">LIGHTING TECHNOLOGY CO.LTD.</div></div>
      <div class="brand__mark"></div>
    </div>
    <div class="brand__ar abs" style="right:40px;top:38px;color:var(--white)"><b>شركة فيلمورا</b><span>لتقنية الإنارة المحدودة</span></div>
    <h1 class="abs head cover__tag">Engineering Lighting Solution Provider</h1>
    <div class="abs cover__rule"></div>
    <div class="photo cover__photo" role="img" aria-label="Photo of an industrial hall lit by LED highbay fixtures"></div>
  </section>

  <section class="page">
    <div class="brand brand--dark" style="left:40px;top:40px">
      <div><div class="brand__name">velmora</div><div class="brand__sub">LIGHTING TECHNOLOGY CO.LTD.</div></div>
      <div class="brand__mark"></div>
    </div>
    <div class="brand__ar abs" style="right:30px;top:38px;color:var(--navy)"><b>شركة فيلمورا</b><span>لتقنية الإنارة المحدودة</span></div>
    <div class="abs about__panel"></div>
    <div class="abs about__band"></div>
    <h2 class="abs head about__title">about us</h2>
    <svg class="abs" style="left:0;top:600px" width="200" height="132" viewBox="0 0 200 132" aria-hidden="true">
      <path d="M30 132 V90 Q30 60 60 60 H200" fill="none" stroke="var(--teal)" stroke-width="1.2"/>
    </svg>
    <div class="abs about__text">
      <p>Velmora lighting technology Co. Ltd is part of Velmora group consisting of Velmora construction and Velmora factory started back in 1995.</p>
      <p>Velmora constructions is specialized in industrial construction activities including civil, mechanical and electrical works. Velmora factory is an electrical accessories manufacturer located in second industrial area, producing electrical metallic pipes and switch boxes.</p>
      <p>Velmora Electrical Accessories Manufacturer started business early in 2003, and has taken care to its customers and maintenance quality ever since. To this end the company employs a highly efficient team with long experience in a variety of specialization. We are confident of executing our work to the highest standards and quality. The company leads in the field of electrical accessories.</p>
    </div>
    <p class="abs head about__quote">Lighting for us is not a Job<span class="q2">it is a Passion</span></p>
  </section>

  <section class="page">
    <div class="photo goals__photo" style="left:46px;top:50px;width:130px;height:115px" role="img" aria-label="Petrochemical plant lit at night"></div>
    <div class="photo goals__photo" style="left:189px;top:50px;width:135px;height:115px" role="img" aria-label="Gas station canopy with LED lights"></div>
    <div class="photo goals__photo" style="left:335px;top:50px;width:138px;height:115px" role="img" aria-label="Industrial facility lit at dusk"></div>
    <div class="photo goals__photo" style="left:46px;top:175px;width:130px;height:146px" role="img" aria-label="Fuel station forecourt at night"></div>
    <div class="photo goals__photo" style="left:189px;top:175px;width:135px;height:146px" role="img" aria-label="Retail interior with LED lighting"></div>
    <div class="photo goals__photo" style="left:335px;top:175px;width:138px;height:146px" role="img" aria-label="Illuminated building facade"></div>
    <div class="photo goals__photo" style="left:335px;top:331px;width:138px;height:146px" role="img" aria-label="Warehouse with highbay lighting"></div>
    <div class="abs goals__band"></div>
    <h2 class="abs head goals__title">Our Goals and mission</h2>
    <p class="abs goals__text">We are not just a company, we are unique solution provider that aims the satisfaction of their clients in every step of the project. We combine the experience with art and engineering to provide a solution that meets the clients requirements. With the help of our high qualified staff, We provide lighting service from A to Z in all manners starting from the lighting design and the products selection, going through the logistic and material handling until the installation part.</p>
  </section>

  <section class="page">
    <div class="refs__grid">
      <div class="refs__cell refs__cell--title"><h2 class="head refs__title" style="position:static">Project<span>References</span></h2></div>
      <div class="refs__cell"><div class="refs__logo"></div><p class="refs__cap">Claritas Highbays And Floodlight Lumora Floodlights</p></div>
      <div class="refs__cell"><div class="refs__logo"></div><p class="refs__cap">Claritas Highbays</p></div>
      <div class="refs__cell"><div class="refs__logo"></div><p class="refs__cap">Claritas Hazardous</p></div>
      <div class="refs__cell"><div class="refs__logo"></div><p class="refs__cap">Velmora LED Highbays</p></div>
      <div class="refs__cell"><div class="refs__logo"></div><p class="refs__cap">Velmora LED Highbays</p></div>
      <div class="refs__cell"><div class="refs__logo"></div><p class="refs__cap">Velmora Highbay And Norvix 60x60 Panels</p></div>
      <div class="refs__cell"><div class="refs__logo"></div><p class="refs__cap">Velmora LED Highbays, LED Tubes</p></div>
      <div class="refs__cell"><div class="refs__logo"></div><p class="refs__cap">Velmora LED Highbays, LED Tubes</p></div>
      <div class="refs__cell"><div class="refs__logo"></div><p class="refs__cap">Velmora LED Floodlights</p></div>
      <div class="refs__cell"><div class="refs__logo"></div><p class="refs__cap">Velmora Highbay And 60x60 Panels</p></div>
      <div class="refs__cell"><div class="refs__logo"></div><p class="refs__cap">Beamcraft Canopy Light, Linear Weatherproof And Streetlight</p></div>
      <div class="refs__cell"><div class="refs__logo refs__logo--c"></div><p class="refs__cap">Beamcraft Canopy Light, Linear Weatherproof And Streetlight, Lumora Downlight, Striplight, 60x60 Panels</p></div>
      <div class="refs__cell"><div class="refs__logo"></div><p class="refs__cap">Beamcraft Canopy Light</p></div>
      <div class="refs__cell"><div class="refs__logo"></div><p class="refs__cap">Lumora LED Mr16 Lamps And Driver, Led Striplights, 60x60 Panels</p></div>
      <div class="refs__cell"><div class="refs__logo"></div><p class="refs__cap">Beamcraft Canopy Light</p></div>
      <div class="refs__cell"><div class="refs__logo"></div><p class="refs__cap">Beamcraft Canopy Light, Linear Weatherproof And Streetlight</p></div>
      <div class="refs__cell"><div class="refs__logo"></div><p class="refs__cap">60x60 Panels, Canopy Lights</p></div>
      <div class="refs__cell"><div class="refs__logo"></div><p class="refs__cap">60x60 Panels, LED Downlights</p></div>
      <div class="refs__cell"><div class="refs__logo"></div><p class="refs__cap">Korvan LED Highbays</p></div>
      <div class="refs__cell"><div class="refs__logo"></div><p class="refs__cap">Korvan LED Highbays</p></div>
      <div class="refs__cell"><p class="refs__cap" style="margin-top:32px">Lumora Striplight And Downlight</p></div>
      <div class="refs__cell"><div class="refs__logo"></div><p class="refs__cap">Lumora LED Lamps, LED Downlight, Led Tubelights</p></div>
    </div>
  </section>

  <section class="page">
    <p class="abs cycle__intro">In each project we go through a pipe line which was built by us among the years to reach the optimum result by the most easiest and efficient way.</p>
    <h2 class="abs head cycle__head"><span class="c1">Projects</span><span class="c2">Cycle</span></h2>
    <div class="abs cycle__spine"></div>

    <div class="step step--l" style="top:140px;color:var(--s1)"><div class="step__title">SITE SURVEY</div><div class="step__box" style="background:var(--s1)">In this stage we collect all the needed data such as facility application, existing lighting system, power consumption, CAD drawings and environment.</div><div class="step__num">1.</div></div>
    <div class="step step--r" style="top:205px;color:var(--s2)"><div class="step__title">LIGHTING DESIGN</div><div class="step__box" style="background:var(--s2)">We put all collected data into the table and we use the latest technology in lighting design Lumicalc to get best solutions.</div><div class="step__num">2.</div></div>
    <div class="step step--l" style="top:262px;color:var(--s3)"><div class="step__title">PROJECT PROPOSAL</div><div class="step__box" style="background:var(--s3)">We make 2 or 3 different solutions that have variation of cost and saving depending on the site and client requirements.</div><div class="step__num">3.</div></div>
    <div class="step step--r" style="top:318px;color:var(--s4)"><div class="step__title">ROI</div><div class="step__box" style="background:var(--s4)">For each and every solution we submit ROI (return of investment) study that explains in deep details the saving and initial cost of the solution and the payback period.</div><div class="step__num">4.</div></div>
    <div class="step step--l" style="top:372px;color:var(--s5)"><div class="step__title">SAMPLES INSTALLATION</div><div class="step__box" style="background:var(--s5)">We always advice our clients to install free of charge samples that will insure our design results and in the same time the client will feel the difference in reality.</div><div class="step__num">5.</div></div>
    <div class="step step--r" style="top:432px;color:var(--s6)"><div class="step__title">LOGISTIC AND DELIVERY</div><div class="step__box" style="background:var(--s6)">We work hand to hand with the supplier and the courier to deliver the goods in the shortest time to all areas updated by all means, regardless of the size or value of the project.</div><div class="step__num">6.</div></div>
    <div class="step step--l" style="top:500px;color:var(--s7)"><div class="step__title">INSTALLATION</div><div class="step__box" style="background:var(--s7)">We will be there in all phases of the project giving all the needed support by the client not only that, we even do turnkey projects if requested by the client.</div><div class="step__num">7.</div></div>
    <div class="step step--r" style="top:555px;color:var(--s8)"><div class="step__title">CUSTOMER TRAINING</div><div class="step__box" style="background:var(--s8)">We provide training for any contractor who will do the job for the end client and we always support them when technical issues pop up.</div><div class="step__num">8.</div></div>
    <div class="step step--l" style="top:622px;color:var(--s9);width:340px"><div class="step__title">AFTER SALES SERVICE</div><div class="step__box" style="background:var(--s9);min-height:30px">We provide warranty and maintenance service to all clients around the country no matter what and where.</div><div class="step__num">9.</div></div>
  </section>

  <section class="page page--navy">
    <div class="brand brand--light" style="left:128px;top:96px;gap:10px">
      <div><div class="brand__name" style="font-size:22px;letter-spacing:4px">velmora</div><div class="brand__sub">LIGHTING TECHNOLOGY CO.LTD.</div></div>
      <div class="brand__mark" style="width:28px;height:28px"></div>
    </div>
    <div class="brand__ar abs" style="left:330px;top:94px;color:var(--white)"><b style="font-size:15px">شركة فيلمورا</b><span style="font-size:7px">لتقنية الإنارة المحدودة</span></div>
    <svg class="abs back__arc" width="520" height="732" viewBox="0 0 520 732" aria-hidden="true">
      <path d="M25 732 V360 Q25 290 95 290 H520" fill="none" stroke="#e6ebf1" stroke-width="1.2"/>
    </svg>
    <div class="abs back__card">
      <div class="abs back__mark"></div>
      <p class="abs back__addr">Kingdom of Saudi Arabia<br>P.O. Box 4410, Eastport 30127<br>Tel./Mobile: +000 555 0142 Fax: 000 555 0198<br>E-mail: sales.led@velmora.example</p>
    </div>
  </section>

</main>
</body>
</html>
```